"Oral Surgery Office needs a Business Card Design with Logo"

We need a logo design and business card. The name of the office is Halvering Oral Surgery & Implant Center. The final design should communicate uniqueness as well as highly class office. The business card should emphasize power. I included the current business card below. Please design something unique

Target Market(s)

Dentists & Patients

Industry/Entity Type

Dental

Contact Information for Business Card

Unique Design to show success, prestige, Style, unmatched performance

Font styles to use
Serif

Colors
1b1b1b
ffffff
0556a4

Requirements
Must have
• Bussiness Name, Doctor's Name, Website, phone and Fax, email, office address
• Color should be either Black and White or Blue and White
Nice to have
• Clean look
Should not have
• the business card shouldn't be too busy. I feel like the old business card was too busy

```html
<!DOCTYPE html>
<html lang="en">
<head>
<meta charset="utf-8">
<title>Halvering Oral Surgery &amp; Implant Center – Business Card</title>
<link rel="stylesheet" href="https://fonts.googleapis.com/css2?family=Montserrat:wght@600;700;800&display=swap">
<style>
  :root {
    --backdrop: #9a9899;
    --ink: #1b1b1b;
    --paper: #ffffff;
    --photo-light: #d9d9d9;
    --photo-mid: #8c8c8c;
    --photo-dark: #3a3a3a;
  }
  * { margin: 0; padding: 0; box-sizing: border-box; }
  html, body { width: 1200px; height: 1000px; overflow: hidden; }
  body {
    background: var(--backdrop);
    font-family: "Montserrat", Arial, sans-serif;
    position: relative;
  }
  .card {
    position: absolute;
    top: 111px;
    height: 659px;
    overflow: hidden;
    box-shadow: 0 1px 3px rgba(0,0,0,0.25);
  }
  .card--front { left: 149px; width: 423px; background: var(--ink); }
  .card--back  { left: 609px; width: 426px; background: var(--ink); }

  .city-photo {
    position: absolute;
    left: 0; top: 0;
    width: 100%; height: 564px;
    background: linear-gradient(180deg, var(--photo-light) 0%, #bdbdbd 18%, var(--photo-mid) 45%, #6a6a6a 75%, var(--photo-dark) 100%);
  }
  .front-name {
    position: absolute;
    left: 0; right: 0; top: 250px;
    text-align: center;
    color: var(--paper);
    font-weight: 800;
    font-size: 50px;
    letter-spacing: 2px;
  }
  .band-title {
    position: absolute;
    right: 22px;
    text-align: right;
    font-weight: 700;
    font-size: 19.5px;
    letter-spacing: 3px;
    line-height: 23px;
  }
  .card--front .band-title { top: 590px; color: var(--paper); }

  .doctor-name {
    position: absolute;
    left: 26px; top: 44px;
    color: var(--paper);
    font-weight: 700;
    font-size: 24px;
    letter-spacing: 3.6px;
  }
  .back-name {
    position: absolute;
    left: 0; right: 0; top: 185px;
    text-align: center;
    color: var(--paper);
    font-weight: 800;
    font-size: 54px;
    letter-spacing: 1px;
  }
  .contact {
    position: absolute;
    left: 26px; top: 428px;
    list-style: none;
    color: var(--paper);
    font-weight: 700;
    font-size: 12px;
    letter-spacing: 2.1px;
    line-height: 19.2px;
  }
  .back-band {
    position: absolute;
    left: 0; bottom: 0;
    width: 100%; height: 94px;
    background: var(--paper);
  }
  .card--back .band-title { top: 588px; color: var(--ink); }
</style>
</head>
<body>
  <section class="card card--front">
    <div class="city-photo" role="img" aria-label="Black and white aerial photograph of a city skyline with skyscrapers"></div>
    <div class="front-name">HALVERING</div>
    <h2 class="band-title">HALVERING ORAL SURGERY<br>&amp; IMPLANT CENTER</h2>
  </section>

  <section class="card card--back">
    <h1 class="doctor-name">DR. MARCUS DELANEY</h1>
    <div class="back-name">HALVERING</div>
    <ul class="contact">
      <li>1840 ALDER ROW</li>
      <li>HALVERING, NY 11590</li>
      <li>TEL: (555) 010 - 4700</li>
      <li>FAX: (555) 010 -5006</li>
      <li>HALVERINGSURGEON@MAILBOX.COM</li>
      <li>WWW.HALVERINGORALSURGERYCENTER.COM</li>
    </ul>
    <div class="back-band"></div>
    <h2 class="band-title">HALVERING ORAL SURGERY<br>&amp; IMPLANT CENTER</h2>
  </section>
</body>
</html>
```